Etiketten für besondere Frauen-Teemischungen
Top Design, zügige Reaktionszeit, sehr netter Kontakt. Alle Wünsche und Anmerkungen wurden perfekt umgesetzt und die Arbeit ist qualitativ hochwertig. Jederzeit gerne wieder! Vielen Dank für das hervorragende Design.
Zielgruppe
Ich stelle Teemischungen speziell für die Schwangerschaft und das Wochenbett sowie für Regelbeschwerden und Wechseljahre her. Zielgruppe sind also Frauen ab Kinderwunsch bis Klimakterium.
Name meiner Unternehmung ist 'Mohn-Quell'
Aufgabenstellung
Ich wünsche mir ein nostalgisches Design, abgelehnt an Apotheken um 1900.
Die Verpackung besteht aus Braunglastiegeln mit schwarzem Bakelitdeckel sowie Glasphiolen mit Korkverschluss.
In den Farben zurückhaltend, nicht knallig. gerne Elfenbein und Lindgrün.
In Anlehnung an den Namen wäre es schön (aber nicht zwingend notwendig), wenn ein Herz dezent eingebunden werden könnte.

```html
<!DOCTYPE html>
<html lang="de">
<head>
<meta charset="utf-8">
<title>Etiketten für Teemischungen – Mohn-Quell</title>
<link href="https://fonts.googleapis.com/css2?family=Oswald:wght@500;600&family=Montserrat:wght@400;600;700&family=Pinyon+Script&family=Libre+Baskerville:ital,wght@1,700&display=swap" rel="stylesheet">
<style>
  :root{
    --page:#ffffff;
    --ivory:#fbfaf1;
    --edge:#e9e7da;
    --ink:#474747;
    --ink-soft:#5a5a5a;
    --ornament:#d6d4c8;
    --heart-a:#8a8a86;
    --heart-b:#c9c8c0;
    --footer:#b9b9b9;
  }
  *{box-sizing:border-box;margin:0;padding:0}
  html,body{width:993px;height:1200px;overflow:hidden;background:var(--page)}
  body{position:relative;font-family:"Montserrat",sans-serif;color:var(--ink)}

  .jar-view{position:absolute;top:245px;transform:scale(.82);transform-origin:top left}
  .jar-view.front{left:323px}
  .jar-view.back{left:580px}

  .label{position:absolute;width:199px;height:199px;background:var(--ivory);border:1px solid var(--edge)}
  .frame{position:absolute;inset:5px;border:2px solid var(--ink)}
  .frame::after{content:"";position:absolute;inset:2px;border:.7px solid var(--ink)}
  .corner{position:absolute;width:16px;height:16px;background:var(--ornament);z-index:1}
  .corner.tl{top:10px;left:10px}.corner.tr{top:10px;right:10px}
  .corner.bl{bottom:10px;left:10px}.corner.br{bottom:10px;right:10px}

  .content{position:absolute;inset:12px 16px;display:flex;flex-direction:column;align-items:center;text-align:center;z-index:2}

  .caps{font-family:"Montserrat",sans-serif;font-weight:700;font-size:4.6px;letter-spacing:1.1px;text-transform:uppercase}
  .brand-line{font-family:"Oswald",sans-serif;font-weight:500;font-size:6px;letter-spacing:2.4px}
  .heart-art{width:32px;height:26px;border-radius:50% 50% 45% 45%;background:radial-gradient(circle at 50% 45%,var(--heart-a),var(--heart-b))}
  .script{font-family:"Pinyon Script",cursive;font-size:7.6px;line-height:1.15;color:var(--ink-soft)}
  .title{font-family:"Oswald",sans-serif;font-weight:600;font-size:17px;letter-spacing:.4px;line-height:1.05}
  .title.xl{font-size:26px;letter-spacing:.8px}
  .since{font-family:"Montserrat",sans-serif;font-size:4.2px;letter-spacing:1.3px}
  .weight{font-family:"Oswald",sans-serif;font-weight:500;font-size:6px;letter-spacing:.6px}

  .heart-row{display:flex;align-items:flex-end;justify-content:space-between;width:100%}
  .foot-row{display:flex;justify-content:space-between;width:100%;margin-top:auto}

  .seal{width:46px;height:46px;border-radius:50%;border:1.4px solid var(--ink);display:flex;align-items:center;justify-content:center;position:relative}
  .seal::before{content:"";position:absolute;inset:3px;border-radius:50%;border:.6px solid var(--ink)}
  .seal-name{font-family:"Oswald",sans-serif;font-weight:600;font-size:8.5px;letter-spacing:.2px}

  /* back side */
  .back-title{font-family:"Oswald",sans-serif;font-weight:600;font-size:11px;letter-spacing:.5px}
  .back-sub{font-family:"Montserrat",sans-serif;font-weight:600;font-size:4.4px;letter-spacing:1.2px;line-height:1.4;text-transform:uppercase;margin-top:2px}
  .body-copy{font-size:3.5px;line-height:1.7;text-align:justify;text-align-last:center;margin-top:4px;width:100%}
  .body-copy b{font-weight:700}
  .claim{font-family:"Libre Baskerville",serif;font-style:italic;font-weight:700;font-size:3.6px;line-height:1.75;text-transform:uppercase;margin-top:5px}
  .batch{width:100%;margin-top:auto;border-top:1.2px solid var(--ink);border-bottom:1.2px solid var(--ink);height:24px;display:flex;align-items:center;justify-content:space-between;padding:0 12px}
  .batch .caps{font-size:3.2px;font-weight:600;letter-spacing:.8px;line-height:1.5}
  .stamp{width:20px;height:20px;border-radius:50%;border:.9px solid var(--ink);background:var(--ivory)}
  .mini-heart{width:20px;height:16px;border-radius:50% 50% 45% 45%;background:radial-gradient(circle at 50% 45%,var(--heart-a),var(--heart-b))}
  .address{font-size:3.4px;line-height:1.5;margin-top:3px}
  .address b{font-weight:700}

  .footer-note{position:absolute;top:1133px;left:0;width:993px;text-align:center;font-size:6.5px;letter-spacing:1.6px;color:var(--footer);text-transform:uppercase}
</style>
</head>
<body>

<!-- Front and back labels as shown on the jars -->
<div class="jar-view front">
  <div class="label" style="left:0;top:0">
    <div class="frame"></div>
    <span class="corner tl" role="img" aria-label="Ornamentale Eckverzierung"></span><span class="corner tr" role="img" aria-label="Ornamentale Eckverzierung"></span>
    <span class="corner bl" role="img" aria-label="Ornamentale Eckverzierung"></span><span class="corner br" role="img" aria-label="Ornamentale Eckverzierung"></span>
    <div class="content">
      <div class="brand-line" style="margin-top:16px">MOHNQUELL</div>
      <div class="heart-row" style="margin-top:3px"><span class="caps" style="margin-bottom:4px">Teemischung</span><span class="heart-art" role="img" aria-label="Herz aus floralen Ornamenten"></span><span class="caps" style="margin-bottom:4px">Für Frauen</span></div>
      <div class="script" style="margin-top:10px">For your health</div>
      <div class="title">SCHWANGERSCHAFT</div>
      <div class="since" style="margin-top:3px">SINCE 2019</div>
      <div class="script" style="margin-top:8px">Teemischung zur Unterstützung<br>eines gesunden Zyklus</div>
      <div class="weight" style="margin-top:8px">50 G ℮</div>
    </div>
  </div>
</div>
<div class="jar-view back">
  <div class="label" style="left:0;top:0">
    <div class="frame"></div>
    <span class="corner tl" role="img" aria-label="Ornamentale Eckverzierung"></span><span class="corner tr" role="img" aria-label="Ornamentale Eckverzierung"></span>
    <span class="corner bl" role="img" aria-label="Ornamentale Eckverzierung"></span><span class="corner br" role="img" aria-label="Ornamentale Eckverzierung"></span>
    <div class="content">
      <div class="back-title" style="margin-top:4px">SCHWANGERSCHAFT</div>
      <div class="back-sub">Teemischung zur Unterstützung<br>eines gesunden Zyklus</div>
      <p class="body-copy">Lorem ipsum dolor sit amet, consetetur sadipscing elitr, sed diam nonumy eirmod tempor invidunt ut labore et dolore magna aliquyam erat, sed diam voluptua at vero eos et accu.<br><b>Zubereitung:</b> Teemischung mit kochendem Wasser aufgießen und 5-8 Minuten ziehen lassen. Nur so erhalten Sie ein sicheres Lebensmittel.<br><b>Zutaten:</b> Kurkuma (42%)*, Apfel (35%)*, Zimt*, Ingwer*, natürliches Aroma, *Zutaten stammen aus ökologischem Landbau</p>
      <p class="claim">Teemischungen speziell für die Schwangerschaft<br>und das Wochenbett sowie für<br>Regelbeschwerden und Wechseljahre.</p>
      <div class="batch"><span class="caps">Mohn-Quell<br>Premium</span><span class="stamp" role="img" aria-label="Siegel"></span><span class="caps">Los-Nr.<br>12345678</span></div>
      <p class="address">Mohn-Quell UG<br>Musterstraße 10 · 12345 Musterstadt<br><b>www.mohn-quell.de</b></p>
    </div>
  </div>
</div>

<!-- Label set, row 1 -->
<div class="label" style="left:71px;top:637px">
  <div class="frame"></div>
  <span class="corner tl" role="img" aria-label="Ornamentale Eckverzierung"></span><span class="corner tr" role="img" aria-label="Ornamentale Eckverzierung"></span>
  <span class="corner bl" role="img" aria-label="Ornamentale Eckverzierung"></span><span class="corner br" role="img" aria-label="Ornamentale Eckverzierung"></span>
  <div class="content">
    <div class="brand-line" style="margin-top:14px">MOHNQUELL</div>
    <div class="heart-row" style="margin-top:3px"><span class="caps" style="margin-bottom:4px">Teemischung</span><span class="heart-art" role="img" aria-label="Herz aus floralen Ornamenten"></span><span class="caps" style="margin-bottom:4px">Für Frauen</span></div>
    <div class="script" style="margin-top:12px">For your health</div>
    <div class="title">SCHWANGERSCHAFT</div>
    <div class="since" style="margin-top:3px">SINCE 2019</div>
    <div class="script" style="margin-top:10px">Teemischung zur Unterstützung<br>eines gesunden Zyklus</div>
    <div class="weight" style="margin-top:10px">50 G ℮</div>
  </div>
</div>

<div class="label" style="left:284px;top:637px">
  <div class="frame"></div>
  <span class="corner tl" role="img" aria-label="Ornamentale Eckverzierung"></span><span class="corner tr" role="img" aria-label="Ornamentale Eckverzierung"></span>
  <span class="corner bl" role="img" aria-label="Ornamentale Eckverzierung"></span><span class="corner br" role="img" aria-label="Ornamentale Eckverzierung"></span>
  <div class="content">
    <div class="back-title" style="margin-top:4px">SCHWANGERSCHAFT</div>
    <div class="back-sub">Teemischung zur Unterstützung<br>eines gesunden Zyklus</div>
    <p class="body-copy">Lorem ipsum dolor sit amet, consetetur sadipscing elitr, sed diam nonumy eirmod tempor invidunt ut labore et dolore magna aliquyam erat, sed diam voluptua at vero eos et accu.<br><b>Zubereitung:</b> Teemischung mit kochendem Wasser aufgießen und 5-8 Minuten ziehen lassen. Nur so erhalten Sie ein sicheres Lebensmittel.<br><b>Zutaten:</b> Kurkuma (42%)*, Apfel (35%)*, Zimt*, Ingwer*, natürliches Aroma, *Zutaten stammen aus ökologischem Landbau</p>
    <p class="claim">Teemischungen speziell für die Schwangerschaft<br>und das Wochenbett sowie für<br>Regelbeschwerden und Wechseljahre.</p>
    <div class="batch"><span class="caps">Mohn-Quell<br>Premium</span><span class="stamp" role="img" aria-label="Siegel"></span><span class="caps">Los-Nr.<br>12345678</span></div>
    <p class="address">Mohn-Quell UG<br>Musterstraße 10 · 12345 Musterstadt<br><b>www.mohn-quell.de</b></p>
  </div>
</div>

<div class="label" style="left:510px;top:637px">
  <div class="frame"></div>
  <div class="content">
    <div class="caps" style="margin-top:8px;font-size:5px">Teemischung für Frauen</div>
    <span class="heart-art" style="margin-top:10px" role="img" aria-label="Herz aus floralen Ornamenten"></span>
    <div class="script" style="margin-top:12px">For your health</div>
    <div class="title xl">MOHN-QUELL</div>
    <div class="since" style="margin-top:3px">SINCE 2019</div>
    <div class="script" style="margin-top:10px">Teemischung zur Unterstützung<br>eines gesunden Zyklus</div>
    <div class="foot-row"><span class="caps">Biologisch</span><span class="caps">Organisch</span></div>
  </div>
</div>

<div class="label" style="left:723px;top:637px">
  <div class="frame"></div>
  <div class="content">
    <div class="back-title" style="margin-top:6px">SCHWANGERSCHAFT</div>
    <div class="back-sub">Teemischung zur Unterstützung<br>eines gesunden Zyklus</div>
    <p class="body-copy">Lorem ipsum dolor sit amet, consetetur sadipscing elitr, sed diam nonumy eirmod tempor invidunt ut labore et dolore magna:<br><b>Zubereitung:</b> Teemischung mit kochendem Wasser aufgießen und 5-8 Minuten ziehen lassen. Nur so erhalten Sie ein sicheres Lebensmittel.<br><b>Zutaten:</b> Kurkuma (42%)*, Apfel (35%)*, Zimt*, Ingwer*, natürliches Aroma, *Zutaten stammen aus ökologischem Landbau</p>
    <p class="claim">Teemischungen speziell für die Schwangerschaft<br>und das Wochenbett sowie für<br>Regelbeschwerden und Wechseljahre.</p>
    <div class="batch"><span class="caps">Mohn-Quell<br>Premium</span><span class="mini-heart" role="img" aria-label="Herz aus floralen Ornamenten"></span><span class="caps">Los-Nr.<br>12345678</span></div>
    <p class="address">Mohn-Quell UG<br>Musterstraße 10 · 12345 Musterstadt<br><b>www.mohn-quell.de</b></p>
  </div>
</div>

<!-- Label set, row 2 -->
<div class="label" style="left:71px;top:877px">
  <div class="frame"></div>
  <span class="corner tl" role="img" aria-label="Ornamentale Eckverzierung"></span><span class="corner tr" role="img" aria-label="Ornamentale Eckverzierung"></span>
  <span class="corner bl" role="img" aria-label="Ornamentale Eckverzierung"></span><span class="corner br" role="img" aria-label="Ornamentale Eckverzierung"></span>
  <div class="content">
    <div class="seal" style="margin-top:2px;width:78px;height:78px"><span class="seal-name" style="font-size:13px">MOHN-QUELL</span></div>
    <div class="title" style="margin-top:12px">SCHWANGERSCHAFT</div>
    <div class="since" style="margin-top:3px;font-weight:600">HIMBEERE HIBISKUS</div>
    <div class="script" style="margin-top:10px">Teemischung zur Unterstützung<br>eines gesunden Zyklus</div>
    <div class="weight" style="margin-top:10px">50 G ℮</div>
  </div>
</div>

<div class="label" style="left:284px;top:877px">
  <div class="frame"></div>
  <span class="corner tl" role="img" aria-label="Ornamentale Eckverzierung"></span><span class="corner tr" role="img" aria-label="Ornamentale Eckverzierung"></span>
  <span class="corner bl" role="img" aria-label="Ornamentale Eckverzierung"></span><span class="corner br" role="img" aria-label="Ornamentale Eckverzierung"></span>
  <div class="content">
    <div class="back-title" style="margin-top:6px">SCHWANGERSCHAFT</div>
    <div class="back-sub">Unterstützung für einen<br>gesunden Zyklus</div>
    <p class="body-copy" style="padding:0 4px">Lorem ipsum dolor sit amet, consetetur sadipscing elitr, sed diam nonumy eirmod tempor invidunt ut labore et dolore magna aliquyam erat, sed diam voluptua. At vero eos et accusam magna aliquyam erat, lorem ipsum dolor sit amet.</p>
    <p class="claim">Teemischungen speziell für die Schwangerschaft<br>und das Wochenbett sowie für<br>Regelbeschwerden und Wechseljahre.</p>
    <div class="batch"><span class="caps">Mohn_Quell<br>Premium</span><span class="stamp" role="img" aria-label="Siegel"></span><span class="caps">Los-Nr.<br>12345678</span></div>
    <p class="address">Mohn-Quell UG<br>Musterstraße 10 · 12345 Musterstadt<br><b>www.mohn-quell.de</b></p>
  </div>
</div>

<div class="label" style="left:510px;top:877px">
  <div class="frame"></div>
  <div class="content">
    <span class="heart-art" style="margin-top:6px" role="img" aria-label="Herz aus floralen Ornamenten"></span>
    <div class="brand-line" style="margin-top:10px;font-size:6.4px">MOHNQUELL</div>
    <div class="script" style="margin-top:10px">For your health</div>
    <div class="title">SCHWANGERSCHAFT</div>
    <div class="since" style="margin-top:3px;font-weight:600">HIMBEERE HIBISKUS</div>
    <div class="script" style="margin-top:12px">Teemischung zur Unterstützung<br>eines gesunden Zyklus</div>
    <div class="weight" style="margin-top:10px">50 G ℮</div>
  </div>
</div>

<div class="label" style="left:723px;top:877px">
  <div class="frame"></div>
  <span class="corner tl" role="img" aria-label="Ornamentale Eckverzierung"></span><span class="corner tr" role="img" aria-label="Ornamentale Eckverzierung"></span>
  <span class="corner bl" role="img" aria-label="Ornamentale Eckverzierung"></span><span class="corner br" role="img" aria-label="Ornamentale Eckverzierung"></span>
  <div class="content">
    <div class="back-title" style="margin-top:4px">SCHWANGERSCHAFT</div>
    <div class="back-sub">Teemischung zur Unterstützung<br>eines gesunden Zyklus</div>
    <p class="body-copy">Lorem ipsum dolor sit amet, consetetur sadipscing elitr, sed diam nonumy eirmod tempor invidunt ut labore et dolore magna aliquyam erat, sed diam voluptua at vero eos et accu.<br><b>Zubereitung:</b> Teemischung mit kochendem Wasser aufgießen und 5-8 Minuten ziehen lassen. Nur so erhalten Sie ein sicheres Lebensmittel.<br><b>Zutaten:</b> Kurkuma (42%)*, Apfel (35%)*, Zimt*, Ingwer*, natürliches Aroma, *Zutaten stammen aus ökologischem Landbau</p>
    <p class="claim">Teemischungen speziell für die Schwangerschaft<br>und das Wochenbett sowie für<br>Regelbeschwerden und Wechseljahre.</p>
    <div class="batch"><span class="caps">Mohn-Quell<br>Premium</span><span class="stamp" role="img" aria-label="Siegel"></span><span class="caps">Los-Nr.<br>12345678</span></div>
    <p class="address">Mohn-Quell UG<br>Musterstraße 10 · 12345 Musterstadt<br><b>www.mohn-quell.de</b></p>
  </div>
</div>

<p class="footer-note">Etiketten für Teemischungen „Mohn-Quell“ · www.mohn-quell.de</p>

</body>
</html>
```